Mara Quintell Fitness

I need a web design for my nutrition/fitness training business. The name of the business is MQ Fitness. I sell fitness programs and do online personal training/nutritional coaching. What I promote right now is my 8 week program and i'm also coming out with a phase two 8 week program. I want to feature both, with paypal links that way people can buy it through my website. I want the website designed around my logo with a black background. And tabs for my program, a tab for an about me section, a tab for me to post a blog, and a tab for my client testimonials/transformations. I want it to be pretty simple and easy to navigate through.
Target Market(s)
Fitness Industry
Industry/Entity Type
Fitness
Number of Pages Required
5+ page
Requirements
Must have
- I made a mock design and put it in the images. I want my website front page to be focused on my logo (which I attached) and also the tabs shown like I have it. Also need a play under my 8 week program tab to let people purchase my separate programs with paypal. Under the blog I just need something that says "coming soon" on that page. And under the about me I attached a picture of my that I want (eating a donut lol) where I want to be able to put a bio next to it.

```html
<!DOCTYPE html>
<html lang="en">
<head>
<meta charset="utf-8">
<title>MQ Fitness</title>
<link href="https://fonts.googleapis.com/css2?family=Open+Sans:wght@400;600;700&family=Raleway:wght@400;600;700&display=swap" rel="stylesheet">
<style>
:root{
  --black:#1b1b1b;
  --nav:#3a3a3a;
  --pink:#e8458b;
  --green:#7dc242;
  --news-green:#74bd44;
  --tan:#dcc39c;
  --white:#ffffff;
  --text:#555555;
  --footer:#262626;
}
*{box-sizing:border-box;margin:0;padding:0}
html,body{width:1200px;height:3028px;overflow:hidden;background:var(--white);font-family:"Open Sans",Arial,sans-serif;color:var(--text)}
.page{width:1200px;height:3028px;position:relative}

.site-header{height:130px;background:var(--black);position:relative}
.brand-name{position:absolute;left:84px;top:46px;font-family:"Open Sans",sans-serif;font-weight:600;font-size:26px;line-height:36px;color:var(--white);letter-spacing:1px}
.lang{position:absolute;right:84px;top:18px;width:96px;height:26px;background:#eee;border-radius:2px;font-size:12px;color:#333;display:flex;align-items:center;padding-left:10px;gap:8px}
.lang span.flag{width:16px;height:11px;background:#c33}

.main-nav{height:42px;background:var(--nav);display:flex;justify-content:center}
.main-nav ul{list-style:none;display:flex;width:1040px}
.main-nav li{font-family:"Raleway",sans-serif;font-weight:600;font-size:14px;color:#ddd;padding:0 28px;line-height:42px;text-transform:uppercase}
.main-nav li.active{background:var(--pink);color:var(--white);padding:0 40px}

.hero{height:548px;position:relative;background:linear-gradient(100deg,#c9b7a6 0%,#e6d9cf 40%,#b9a99a 70%,#8d847c 100%)}
.hero-arrow{position:absolute;top:250px;width:44px;height:44px;border-radius:50%;background:rgba(0,0,0,.35)}
.hero-arrow.prev{left:60px}.hero-arrow.next{right:60px}
.hero-arrow svg{width:44px;height:44px}

.section-title{font-family:"Raleway",sans-serif;font-weight:600;font-size:36px;text-align:center;text-transform:uppercase;letter-spacing:1px;color:#333}
.section-title em{font-style:normal;color:var(--pink)}
.title-rule{width:70px;height:3px;background:var(--pink);margin:12px auto 0}

.welcome{height:310px;padding-top:44px;text-align:center}
.welcome p{width:1000px;margin:30px auto 0;font-size:15px;line-height:24px}
.btn{display:inline-block;font-size:12px;font-weight:700;text-transform:uppercase;color:var(--white);padding:9px 26px;border-radius:2px}
.btn-pink{background:var(--pink);margin-top:22px}
.btn-green{background:var(--green)}
.btn-white{background:var(--white);color:#333}

.program{height:448px;background:var(--tan);padding-top:48px;position:relative}
.program .section-title{color:var(--white);font-weight:400}
.program .section-title em{color:var(--white);font-weight:700}
.program-cards{display:flex;gap:40px;justify-content:center;margin-top:40px}
.program-card{width:508px;height:252px;background:var(--white);display:flex;padding:26px;gap:24px}
.program-photo{width:220px;height:200px;flex:none}
.program-card h3{font-family:"Raleway",sans-serif;font-weight:600;font-size:26px;color:var(--green);text-transform:uppercase;margin-top:4px}
.program-card p{font-size:14px;line-height:22px;margin:14px 0 18px}
.slider-dots{display:flex;gap:8px;justify-content:center;margin-top:24px}
.slider-dots span{width:18px;height:18px;border-radius:50%;background:#777}

.featured{height:500px;padding-top:48px;text-align:center}
.video-frame{width:780px;height:328px;margin:46px auto 0;position:relative;background:linear-gradient(90deg,#6b7077 0%,#9aa0a6 45%,#c9a98c 75%,#8a6f5e 100%)}
.play{position:absolute;left:362px;top:136px;width:56px;height:56px}

.news{height:360px;background:var(--news-green);padding-top:50px}
.news .section-title{color:var(--white);font-weight:400}
.news .section-title em{color:var(--white)}
.news .title-rule{background:var(--white)}
.news-list{display:flex;gap:60px;justify-content:center;margin-top:44px}
.news-item{width:470px;display:flex;gap:24px;color:var(--white)}
.news-date{text-align:center;flex:none;width:80px}
.news-date b{display:block;font-size:38px;font-weight:600;line-height:40px}
.news-date small{font-size:12px}
.news-item p{font-size:14px;line-height:21px}
.news-item .btn{margin-top:16px}

.gallery{height:542px;padding-top:44px}
.gallery-grid{display:grid;grid-template-columns:repeat(4,254px);gap:12px;justify-content:center;margin-top:42px}
.gallery-grid div{height:184px}

.site-footer{position:absolute;left:0;top:2880px;width:1200px;height:148px;background:var(--footer);color:#bbb;font-size:12px}
.social{position:absolute;left:72px;top:34px;display:flex;gap:8px}
.social span{width:24px;height:24px;border-radius:50%;background:#ddd}
.copyright{position:absolute;left:72px;top:76px}
.pay{position:absolute;left:500px;top:28px}
.pay h4,.contact h4{color:var(--white);font-size:14px;font-weight:600;margin-bottom:12px}
.pay-badges{display:flex;gap:6px}
.pay-badges span{width:34px;height:22px;background:#e6e6e6;border-radius:2px}
.contact{position:absolute;left:880px;top:28px;padding-left:30px}
.contact svg{position:absolute;left:0;top:0}
.contact p{line-height:18px}
.contact .phone{color:var(--white);font-size:15px;font-weight:600;margin-top:6px}
</style>
</head>
<body>
<div class="page">
  <header class="site-header">
    <span class="brand-name">MQ Fitness</span>
    <div class="lang"><span class="flag"></span>English</div>
  </header>
  <nav class="main-nav">
    <ul>
      <li class="active">Home</li><li>About Us</li><li>My 8 Week Program</li><li>Blog</li><li>Transformations</li><li>Contact Us</li>
    </ul>
  </nav>

  <section class="hero" role="img" aria-label="Photo of women training with dumbbells in a bright gym">
    <span class="hero-arrow prev"><svg viewBox="0 0 44 44"><path d="M25 14l-8 8 8 8" stroke="#fff" stroke-width="3" fill="none"/></svg></span>
    <span class="hero-arrow next"><svg viewBox="0 0 44 44"><path d="M19 14l8 8-8 8" stroke="#fff" stroke-width="3" fill="none"/></svg></span>
  </section>

  <section class="welcome">
    <h2 class="section-title">Welcome to our <em>site</em></h2>
    <div class="title-rule"></div>
    <p>Welcome to a place built for real results. Our coaching blends smart training, simple nutrition and steady support so you can build strength, lose fat and feel confident every day. Whether you are just starting out or ready for your next challenge, each program is planned to fit your schedule, your goals and your life. Train at home or in the gym and track progress with clear weekly steps.</p>
    <span class="btn btn-pink">Read More</span>
  </section>

  <section class="program">
    <h2 class="section-title">8 Week <em>Program</em></h2>
    <div class="program-cards">
      <article class="program-card">
        <div class="program-photo" role="img" aria-label="Photo of a woman doing a core workout" style="background:linear-gradient(135deg,#c7a48a,#7a5a4a)"></div>
        <div><h3>Phase I</h3><p>Eight weeks of guided workouts and meal plans to build a strong base and lasting habits.</p><span class="btn btn-green">Buy</span></div>
      </article>
      <article class="program-card">
        <div class="program-photo" role="img" aria-label="Photo of a man doing push-ups outdoors" style="background:linear-gradient(135deg,#9fb8cc,#c9b8a3)"></div>
        <div><h3>Phase II</h3><p>The next eight weeks raise the intensity with new lifts, intervals and refined nutrition.</p><span class="btn btn-green">Buy</span></div>
      </article>
    </div>
    <div class="slider-dots"><span></span><span></span></div>
  </section>

  <section class="featured">
    <h2 class="section-title">Featured <em>Video</em></h2>
    <div class="title-rule"></div>
    <div class="video-frame" role="img" aria-label="Video still of a woman training outdoors beside a truck">
      <svg class="play" viewBox="0 0 56 56"><circle cx="28" cy="28" r="28" fill="rgba(0,0,0,.6)"/><path d="M22 17l18 11-18 11z" fill="#fff"/></svg>
    </div>
  </section>

  <section class="news">
    <h2 class="section-title">Latest <em>News</em></h2>
    <div class="title-rule"></div>
    <div class="news-list">
      <article class="news-item">
        <div class="news-date"><b>02</b><small>AUG 2015</small></div>
        <div><p>Simple swaps for a cleaner plate: five easy changes to your daily meals that support fat loss without leaving you hungry.</p><span class="btn btn-white">Read More</span></div>
      </article>
      <article class="news-item">
        <div class="news-date"><b>16</b><small>AUG 2015</small></div>
        <div><p>Client spotlight: how consistent training three days a week led to real strength gains and a new level of confidence.</p><span class="btn btn-white">Read More</span></div>
      </article>
    </div>
  </section>

  <section class="gallery">
    <h2 class="section-title">Our <em>Gallery</em></h2>
    <div class="title-rule"></div>
    <div class="gallery-grid">
      <div role="img" aria-label="Gym training photo" style="background:linear-gradient(135deg,#5a5a5a,#333)"></div>
      <div role="img" aria-label="Kettlebell workout photo" style="background:linear-gradient(135deg,#8a6a55,#3e2f28)"></div>
      <div role="img" aria-label="Personal trainer coaching photo" style="background:linear-gradient(135deg,#b9a38f,#6e5a4b)"></div>
      <div role="img" aria-label="Stretching class photo" style="background:linear-gradient(135deg,#e2ddd6,#a9a09a)"></div>
      <div role="img" aria-label="Core exercise photo" style="background:linear-gradient(135deg,#c8c2ba,#6b6660)"></div>
      <div role="img" aria-label="Group fitness photo" style="background:linear-gradient(135deg,#d7c9c2,#8c8e96)"></div>
      <div role="img" aria-label="Indoor cycling photo" style="background:linear-gradient(135deg,#7b6f68,#2e2a28)"></div>
      <div role="img" aria-label="Bench workout photo" style="background:linear-gradient(135deg,#d9d4cf,#8a7d74)"></div>
    </div>
  </section>

  <footer class="site-footer">
    <div class="social"><span></span><span></span><span></span><span></span><span></span><span></span></div>
    <p class="copyright">Copyright © 2015 MQ Fitness. Privacy Policy | Terms &amp; Conditions</p>
    <div class="pay"><h4>Pay Through</h4><div class="pay-badges"><span></span><span></span><span></span><span></span></div></div>
    <div class="contact">
      <svg width="18" height="24" viewBox="0 0 18 24"><path d="M9 0a9 9 0 0 0-9 9c0 7 9 15 9 15s9-8 9-15a9 9 0 0 0-9-9z" fill="#fff"/><circle cx="9" cy="9" r="3.5" fill="#262626"/></svg>
      <h4>Contact Us</h4>
      <p>2240 Harrow Street, Denver CO 80203</p>
      <p class="phone">+1 800 555 0142</p>
    </div>
  </footer>
</div>
</body>
</html>
```